Flyer Design for catering company "Rosemary's Larder"

We need a flyer design for a small catering company based in Melbourne, Australia called Rosemary's Larder. We are in the process of re-branding at the moment and want to use the new brand for the logo. The new website is still under development but you can have a look at it here: http://rosemaryslarder.sitevane.net/minimal-layout The product we want to market i the flyer are our ready-made meals. We are marketing to the corporate world. The meals are intended to be purchased by large firms to feed their staff that are working back late after-hours. They are home-made, fresh, healthy, convenient and most importantly - delicious! You can find the menu and a brief explanation of the ready-made meals on the website. I thought that we might include the menu on the backside of the flyer but i am not set on this.

We want to provide an introductory offer of 10 meals for $100 (usually $130).

I have attached an image of where i got to with the flyer just for your information. You can see why i need your assistance!

I should also add that the logo is intended to be printed in a gold foil! Added Wednesday, February 3, 2016

Target Market(s)

Corporate market - this doesnt mean boring though. It wont be the big bosses who read this flyer it will be the catering managers - they are likely to see a lot of flyers so this one needs to stand out.

Industry/Entity Type

Catering

Requirements
Must have
• Must have the logo! Keep in mind the logo will be printed in a gold foil so it will be very metallic.
• Must reference introductory offer of 10 meals for $100.
• Must have website.
Nice to have
• Would like to see the menu on the backside - i am flexible with this if you have a better idea.
Should not have
• no cartoony images

```html
<!DOCTYPE html>
<html lang="en">
<head>
<meta charset="utf-8">
<title>Rosemary's Larder – Ready-Made Meals Flyer</title>
<link rel="stylesheet" href="https://fonts.googleapis.com/css2?family=Montserrat:wght@400;600;700&display=swap">
<style>
  :root {
    --backdrop: #c9c9c9;
    --paper-edge: #ffffff;
    --plum-light: #8a5565;
    --plum: #6b3c4b;
    --plum-dark: #46242f;
    --rose: #c9899b;
    --rose-pale: rgba(230, 190, 200, 0.35);
    --stripe: rgba(255, 255, 255, 0.07);
    --ribbon: #5c3e6c;
    --ribbon-dark: #3f2a4c;
    --gold: #b9a23c;
    --gold-light: #d6c25a;
    --ink-light: #f3e6ea;
    --ink-muted: #e2cbd2;
    --ink-dark: #2c1a20;
  }
  * { box-sizing: border-box; margin: 0; padding: 0; }
  html, body { width: 1200px; height: 542px; overflow: hidden; }
  body {
    background: var(--backdrop);
    font-family: "Montserrat", Arial, sans-serif;
    display: flex;
    align-items: center;
    justify-content: center;
    gap: 80px;
  }
  .flyer {
    position: relative;
    width: 354px;
    height: 500px;
    border: 6px solid var(--paper-edge);
    background: linear-gradient(160deg, var(--plum-light) 0%, var(--plum) 45%, var(--plum-dark) 100%);
    overflow: hidden;
    color: var(--ink-light);
  }

  /* ---------- Front ---------- */
  .front__photo { position: absolute; top: 0; left: 0; }
  .logo-badge {
    position: absolute;
    border-radius: 50%;
    background: radial-gradient(circle at 35% 30%, var(--gold-light), var(--gold) 70%);
    border: 3px solid var(--paper-edge);
    display: flex;
    align-items: center;
    justify-content: center;
    text-align: center;
  }
  .logo-badge__name {
    font-weight: 600;
    color: var(--paper-edge);
    line-height: 1.15;
  }
  .front .logo-badge { width: 128px; height: 128px; top: 130px; right: 26px; }
  .front .logo-badge__name { font-size: 16px; }

  .ribbon {
    position: absolute;
    left: 50%;
    transform: translateX(-50%);
    background: var(--ribbon);
    color: var(--ink-light);
    font-weight: 700;
    text-transform: uppercase;
    letter-spacing: 0.5px;
    padding: 6px 26px;
    white-space: nowrap;
    clip-path: polygon(0 0, 100% 0, 94% 50%, 100% 100%, 0 100%, 6% 50%);
  }
  .ribbon--offer { top: 288px; font-size: 13px; }
  .ribbon--price { top: 320px; font-size: 16px; background: var(--ribbon-dark); }

  .front__copy {
    position: absolute;
    top: 362px;
    left: 30px;
    right: 30px;
    text-align: center;
    font-size: 8.5px;
    line-height: 1.45;
    text-transform: uppercase;
    color: var(--ink-muted);
  }
  .front__copy p + p { margin-top: 5px; }

  .web-band {
    position: absolute;
    left: 18px;
    right: 18px;
    bottom: 14px;
    padding: 8px 0;
    text-align: center;
    background: var(--rose-pale);
    font-size: 9.5px;
    font-weight: 600;
    letter-spacing: 0.5px;
    color: var(--ink-light);
  }

  /* ---------- Back ---------- */
  .back {
    background:
      repeating-linear-gradient(172deg, transparent 0 22px, var(--stripe) 22px 34px),
      linear-gradient(165deg, var(--plum-light) 0%, var(--rose) 55%, var(--plum) 100%);
  }
  .menu-heading {
    position: absolute;
    top: 16px;
    left: 14px;
    width: 220px;
    padding: 4px 8px;
    font-size: 9px;
    font-weight: 700;
    color: var(--ink-light);
    background: linear-gradient(90deg, var(--ribbon) 0%, var(--rose) 100%);
    border: 1px solid var(--ink-light);
    clip-path: polygon(0 0, 100% 0, 94% 50%, 100% 100%, 0 100%);
  }
  .menu {
    position: absolute;
    top: 42px;
    left: 18px;
    right: 18px;
    list-style: none;
  }
  .menu__item { margin-bottom: 5px; }
  .menu__name {
    font-size: 7.5px;
    font-weight: 700;
    color: var(--ink-dark);
    text-transform: uppercase;
    margin-bottom: 3px;
  }
  .menu__desc {
    font-size: 7px;
    line-height: 1.4;
    color: var(--ink-light);
    padding-left: 4px;
  }
  .menu__note {
    font-size: 7px;
    line-height: 1.4;
    color: var(--ink-light);
    padding-left: 4px;
    margin: 4px 0 7px;
  }
  .back .logo-badge { width: 80px; height: 80px; bottom: 56px; right: 14px; }
  .back .logo-badge__name { font-size: 10px; }
</style>
</head>
<body>

  <!-- Front side -->
  <section class="flyer front">
    <svg class="front__photo" width="342" height="300" viewBox="0 0 342 300" role="img" aria-label="Photograph of bagels, strawberries and boxed ready-made meals">
      <defs>
        <linearGradient id="photoTones" x1="0" y1="0" x2="1" y2="1">
          <stop offset="0" stop-color="#b58a5c"/>
          <stop offset="0.5" stop-color="#8a5a36"/>
          <stop offset="1" stop-color="#c7b7a6"/>
        </linearGradient>
      </defs>
      <path d="M0 0 H342 V40 C280 70 220 110 200 170 C180 235 110 270 0 292 Z" fill="url(#photoTones)"/>
    </svg>

    <div class="logo-badge">
      <span class="logo-badge__name">Rosemary's<br>Larder</span>
    </div>

    <div class="ribbon ribbon--offer">Introductory offer!</div>
    <div class="ribbon ribbon--price">10 meals for $100!</div>

    <div class="front__copy">
      <p>Looking for a way to keep your staff working hard after hours? We have the solution.</p>
      <p>Our home-made meals are a great, convenient solution. With our meals on hand, your staff will never go hungry on those late nights at the office.</p>
    </div>

    <div class="web-band">VISIT WWW.ROSEMARYSLARDER.COM.AU</div>
  </section>

  <!-- Back side -->
  <section class="flyer back">
    <h2 class="menu-heading">TRADITIONAL DISHES</h2>
    <ul class="menu">
      <li class="menu__item">
        <p class="menu__name">Traditional Lasagne</p>
        <p class="menu__desc">Beef lasagne with a creamy béchamel sauce</p>
      </li>
      <li class="menu__item">
        <p class="menu__desc">Pork and veal meatballs</p>
        <p class="menu__desc">Pork &amp; veal meatballs in a rich tomato passata with risoni &amp; green beans</p>
      </li>
      <li class="menu__item">
        <p class="menu__name">Thai Red Beef Curry</p>
        <p class="menu__desc">Slow cooked red beef curry with basmati rice</p>
      </li>
      <li class="menu__item">
        <p class="menu__name">Spinach &amp; Ricotta Cannelloni (Vegetarian)</p>
        <p class="menu__desc">Spinach, ricotta &amp; pumpkin cannelloni with a rich tomato passata</p>
      </li>
      <li class="menu__item">
        <p class="menu__name">Chicken Risotto (Gluten Free)</p>
        <p class="menu__desc">Traditional risotto made with chicken, fresh vegetables and Arborio rice</p>
      </li>
      <li>
        <p class="menu__note">HEALTHY OPTIONS – All of our home made meals are good for you, but these meals are designed for the health conscious among us!</p>
      </li>
      <li class="menu__item">
        <p class="menu__name">Shepherd's Pie (Gluten Free)</p>
        <p class="menu__desc">A low carb version of the classic British dish made with minced lamb and covered with a delicious sweet potato and potato mash</p>
      </li>
      <li class="menu__item">
        <p class="menu__name">Chicken Cacciatore (Gluten Free)</p>
        <p class="menu__desc">An Italian dish of chicken braised in a tomato-based sauce with olives, herbs and vegetables and served on a bed of sweet potato and pumpkin mash</p>
      </li>
      <li class="menu__item">
        <p class="menu__name">Chickpea &amp; Pumpkin Yellow Curry (Vegetarian, Gluten Free)</p>
        <p class="menu__desc">A fragrant yet milk yellow curry made with chickpeas, pumpkin and spinach, served on a bed of brown rice</p>
      </li>
      <li class="menu__item">
        <p class="menu__name">Moroccan Vegetable Tagine (Vegetarian)</p>
        <p class="menu__desc">A traditional Moroccan stew made with a variety of fresh vegetables and served on a bed of wholemeal couscous</p>
      </li>
    </ul>

    <div class="logo-badge">
      <span class="logo-badge__name">Rosemary's<br>Larder</span>
    </div>

    <div class="web-band">VISIT WWW.ROSEMARYSLARDER.COM.AU</div>
  </section>

</body>
</html>
```